exclusive Speakeasy Bar Web design in New Jersey USA

We are opening a speakeasy in New Jersey USA soon. we are looking for a web designer to do our web site including the coding. we a looking for a 4 to 5 page web design. the site will be mostly static. home page, contact page, menu page and a link to a 3rd party site (most likely Qelmo) for reservations. we are looking for this designer to do our menu deign as well. we are looking for a quick turnaround 7-10 days. i am attaching some pictures for the designers to see the concept design and the actual current pictures with our logo as well. professionally taken pictures will be provided later on. our photographer will be taking the pictures in the next week.

Industry/Entity Type

Restaurant, Bar, Speakeasy

Coding

Coded - Design and coding required

Number of Pages Required

4 page

Requirements
Must have
• home page, contact page, menu page and a link to qelmo.com for reservations
Nice to have
• some videos

```html
<!DOCTYPE html>
<html lang="en">
<head>
<meta charset="utf-8">
<title>218 Parlor — Web Design</title>
<link href="https://fonts.googleapis.com/css2?family=Poppins:wght@400;600;700&family=Playfair+Display:wght@700;800&display=swap" rel="stylesheet">
<style>
:root{
  --gold:#b08339;
  --gold-soft:#c49a52;
  --ink:#0b1116;
  --white:#ffffff;
  --rule:#5c6670;
  --sans:'Poppins',sans-serif;
  --serif:'Playfair Display',serif;
}
*{margin:0;padding:0;box-sizing:border-box}
html,body{width:669px;height:1200px;overflow:hidden}
body{background:var(--gold);position:relative;font-family:var(--sans);color:var(--white)}
.section-label{position:absolute;left:54px;font-size:5.8px;font-weight:700;letter-spacing:.1px}
.board{position:absolute;left:34px;width:602px;height:386px;background:var(--ink);box-shadow:0 3px 8px rgba(0,0,0,.25);overflow:hidden}
.board-home{top:70px}
.board-menu{top:517px}
.sidebar{position:absolute;left:0;top:0;width:198px;height:100%}
.board-menu .sidebar{border-right:1px solid var(--gold)}
.brand-mark{position:absolute;left:22px;top:36px;font-family:var(--serif);font-size:8px;font-weight:700;color:var(--white);line-height:1.1}
.eyebrow{position:absolute;left:22px;top:157px;font-size:6.5px;color:var(--gold);letter-spacing:.1px}
.headline{position:absolute;left:22px;top:172px;font-family:var(--serif);font-weight:800;font-size:17px;line-height:29px;color:var(--white)}
.cta-arrow{position:absolute;left:22px;top:259px}
.cta{position:absolute;left:73px;top:254px;width:125px;height:20px;background:var(--gold);display:flex;align-items:center;padding-left:10px;font-size:7px;color:var(--white)}
.cta .partner{margin-left:10px;font-size:4.5px;font-weight:700;letter-spacing:.6px;color:var(--white)}
.socials{position:absolute;left:22px;top:344px;display:flex;gap:10px}
.socials span{font-size:5px;font-weight:600;color:var(--gold);display:flex;align-items:center;gap:2px}
.socials span::before{content:"";width:6px;height:6px;border:1px solid var(--gold)}
.copyright{position:absolute;left:22px;top:369px;font-size:4.6px;color:var(--gold)}
.stage{position:absolute;left:198px;top:0;width:404px;height:100%}
.stage-photo{background:radial-gradient(ellipse at 50% 30%,#4d6a75 0%,#2b3a44 40%,#1a1c24 70%),linear-gradient(#1b1d22,#3a2d27)}
.stage-photo::after{content:"";position:absolute;left:0;right:0;bottom:0;height:45%;background:linear-gradient(transparent,rgba(70,50,38,.8))}
.nav{position:absolute;top:40px;left:0;width:100%;height:10px}
.nav a{position:absolute;font-size:4.8px;font-weight:700;color:var(--white);text-decoration:none;letter-spacing:.1px}
.nav a.active::after{content:"";position:absolute;left:-3px;right:-3px;top:9px;height:1px;background:var(--gold)}
.nav-btn{position:absolute;left:311px;top:33px;width:70px;height:20px;background:var(--gold);display:flex;align-items:center;justify-content:center;font-size:4.6px;font-weight:700;color:var(--white)}
.play{position:absolute;left:182px;top:172px;width:40px;height:40px;border-radius:50%;background:rgba(210,210,210,.85);z-index:2;display:flex;align-items:center;justify-content:center}
.slider-prev{position:absolute;left:333px;top:345px;z-index:2}
.slider-next{position:absolute;left:355px;top:341px;width:25px;height:19px;background:var(--gold);z-index:2;display:flex;align-items:center;justify-content:center}
.menu-kicker{position:absolute;left:0;width:100%;top:83px;text-align:center;font-size:4.6px;font-weight:600;color:var(--gold)}
.menu-title{position:absolute;left:0;width:100%;top:94px;text-align:center;font-family:var(--serif);font-size:7.2px;font-weight:700;color:var(--white)}
.menu-list{position:absolute;left:15px;top:120px;width:368px;list-style:none}
.menu-item{display:flex;align-items:center;height:20px;font-size:5.6px;font-weight:600;color:#e3e5e8}
.menu-item .leader{flex:1;margin:0 4px;border-top:1px double var(--rule);height:2px;border-bottom:1px solid var(--rule)}
.menu-item .price{width:26px}
.identity{position:absolute;left:267px;top:964px;width:136px;height:178px;border:2px solid var(--gold-soft);display:flex;flex-direction:column;align-items:center;justify-content:center;font-family:var(--serif);font-weight:700;color:var(--white);text-align:center}
.identity .num{font-size:50px;line-height:1}
.identity .word{font-size:16px;letter-spacing:2px;margin-top:6px}
</style>
</head>
<body>

<div class="section-label" style="top:48px">HOMEPAGE</div>
<section class="board board-home">
  <div class="sidebar">
    <div class="brand-mark">218<br>PARLOR</div>
    <div class="eyebrow">218 PARLOR</div>
    <h1 class="headline">New Jersey Best<br>Speakeasy</h1>
    <svg class="cta-arrow" width="42" height="8" viewBox="0 0 42 8"><line x1="0" y1="4" x2="40" y2="4" stroke="#fff" stroke-width=".8"/><polyline points="37,1 40.5,4 37,7" fill="none" stroke="#fff" stroke-width=".8"/></svg>
    <div class="cta">Reserve Table on Qelmo<span class="partner">QELMO</span></div>
    <div class="socials"><span>Lumo</span><span>Chirp</span><span>Facet</span></div>
    <div class="copyright">All Rights Reserved 218 parlor © 2023</div>
  </div>
  <div class="stage stage-photo" role="img" aria-label="Lounge interior with curved velvet booths, globe chandeliers and a glowing blue wall">
    <nav class="nav" style="z-index:2">
      <a class="active" style="left:47px">HOME</a><a style="left:81px">ABOUT</a><a style="left:117px">MENU</a><a style="left:151px">RESERVATION</a><a style="left:204px">CONTACT</a>
    </nav>
    <div class="nav-btn" style="z-index:2">RESERVE ON QELMO</div>
    <div class="play"><svg width="12" height="12" viewBox="0 0 12 12"><polygon points="3,1 11,6 3,11" fill="#b08339"/></svg></div>
    <svg class="slider-prev" width="6" height="8" viewBox="0 0 6 8"><polyline points="5,1 1.5,4 5,7" fill="none" stroke="#fff" stroke-width="1"/></svg>
    <div class="slider-next"><svg width="6" height="8" viewBox="0 0 6 8"><polyline points="1,1 4.5,4 1,7" fill="none" stroke="#fff" stroke-width="1"/></svg></div>
  </div>
</section>

<div class="section-label" style="top:492px">MENU PAGE</div>
<section class="board board-menu">
  <div class="sidebar">
    <div class="brand-mark">218<br>PARLOR</div>
    <div class="eyebrow">218 PARLOR</div>
    <h1 class="headline">New Jersey Best<br>Speakeasy</h1>
    <svg class="cta-arrow" width="42" height="8" viewBox="0 0 42 8"><line x1="0" y1="4" x2="40" y2="4" stroke="#fff" stroke-width=".8"/><polyline points="37,1 40.5,4 37,7" fill="none" stroke="#fff" stroke-width=".8"/></svg>
    <div class="cta">Reserve Table on Qelmo<span class="partner">QELMO</span></div>
    <div class="socials"><span>Lumo</span><span>Chirp</span><span>Facet</span></div>
    <div class="copyright">All Rights Reserved 218 parlor © 2023</div>
  </div>
  <div class="stage">
    <nav class="nav">
      <a style="left:47px">HOME</a><a style="left:81px">ABOUT</a><a class="active" style="left:117px">MENU</a><a style="left:151px">RESERVATION</a><a style="left:204px">CONTACT</a>
    </nav>
    <div class="nav-btn">RESERVE ON QELMO</div>
    <div class="menu-kicker">DRINKS</div>
    <h2 class="menu-title">OUR SPECIALS</h2>
    <ul class="menu-list">
      <li class="menu-item"><span>LOREM IPSUM DOLOR</span><span class="leader"></span><span class="price">$ 150.00</span></li>
      <li class="menu-item"><span>CONSECTETUR ADIPISCING</span><span class="leader"></span><span class="price">$ 142.00</span></li>
      <li class="menu-item"><span>NULLA ALIQUET</span><span class="leader"></span><span class="price">$ 300.00</span></li>
      <li class="menu-item"><span>TEMPUS EGESTAS</span><span class="leader"></span><span class="price">$ 180.00</span></li>
      <li class="menu-item"><span>NIBH TORTOR</span><span class="leader"></span><span class="price">$ 130.00</span></li>
      <li class="menu-item"><span>FRINGILLA EST</span><span class="leader"></span><span class="price">$ 100.00</span></li>
      <li class="menu-item"><span>LECTUS PROIN</span><span class="leader"></span><span class="price">$ 110.00</span></li>
      <li class="menu-item"><span>SOLLICITUDIN ALIQUAM</span><span class="leader"></span><span class="price">$ 150.00</span></li>
      <li class="menu-item"><span>MAURIS SIT</span><span class="leader"></span><span class="price">$ 190.00</span></li>
      <li class="menu-item"><span>DUIS AT</span><span class="leader"></span><span class="price">$ 150.00</span></li>
    </ul>
    <svg class="slider-prev" width="6" height="8" viewBox="0 0 6 8"><polyline points="5,1 1.5,4 5,7" fill="none" stroke="#fff" stroke-width="1"/></svg>
    <div class="slider-next"><svg width="6" height="8" viewBox="0 0 6 8"><polyline points="1,1 4.5,4 1,7" fill="none" stroke="#fff" stroke-width="1"/></svg></div>
  </div>
</section>

<div class="identity"><span class="num">218</span><span class="word">PARLOR</span></div>

</body>
</html>
```